Business Card Design Project

Business card design using our logo, consistent with website branding (www.brightquill.com.au) and includes our services:

advertising|sales|events|production

Details Required:

Marcus Dunne
Managing Director

P 1300 586 231
M 0407 862 553
F (02) 8361 2490
E marcus@brightquill.com.au
W www.brightquill.com.au

Will be printed on high quality card with rounded corners.

Quick turnaround required, on standby for any questions to assist with this.

Will upload logo and previous drafts we didn't think were the right fit.

Target Market(s)

Senior business decision-makers

Industry/Entity Type

Business

Requirements
Must have
• Editable template, so details can be updated for staff

Must be in print ready format - please see specs I have just uploaded

```html
<!DOCTYPE html>
<html lang="en">
<head>
<meta charset="utf-8">
<title>BrightQuill Business Card</title>
<link href="https://fonts.googleapis.com/css2?family=Arimo:wght@400;700&family=Questrial&display=swap" rel="stylesheet">
<style>
  :root {
    --stage: #2e2e2e;
    --card: #f4f4f4;
    --card-edge: #ffffff;
    --ink: #3a3a3a;
    --ink-soft: #555555;
    --accent-orange: #ee6a1f;
    --accent-blue: #1e8fd6;
    --accent-gold: #f6a623;
  }
  * { box-sizing: border-box; margin: 0; padding: 0; }
  html, body { width: 1200px; height: 456px; overflow: hidden; }
  body { background: var(--stage); position: relative; font-family: "Arimo", Arial, sans-serif; }

  .card {
    position: absolute;
    top: 84px;
    width: 514px;
    height: 286px;
    border-radius: 22px;
    background: radial-gradient(ellipse at 50% 45%, var(--card-edge) 0%, var(--card) 75%, #e9e9e9 100%);
    box-shadow: 0 4px 14px rgba(0,0,0,.45);
  }
  .card--front { left: 72px; }
  .card--back { left: 615px; }

  .brand { position: absolute; display: flex; align-items: center; }
  .brand__dot { border-radius: 50%; background: var(--accent-gold); flex: none; }
  .brand__name { font-family: "Questrial", "Century Gothic", sans-serif; color: var(--ink); line-height: 1; white-space: nowrap; }
  .brand__tagline {
    position: absolute;
    font-family: "Questrial", "Century Gothic", sans-serif;
    color: var(--ink-soft);
    white-space: nowrap;
  }

  .card--front .brand { left: 100px; top: 114px; }
  .card--front .brand__dot { width: 50px; height: 50px; margin-right: 22px; }
  .card--front .brand__name { font-size: 52px; }
  .card--front .brand__tagline { left: 211px; top: 172px; font-size: 9.5px; letter-spacing: 3px; }

  .services {
    position: absolute;
    left: 0; right: 0; top: 251px;
    text-align: center;
    font-family: "Questrial", "Century Gothic", sans-serif;
    font-size: 10px;
    letter-spacing: 4.3px;
    color: var(--ink);
    white-space: nowrap;
  }

  .card--back .brand { left: 80px; top: 62px; }
  .card--back .brand__dot { width: 36px; height: 36px; margin-right: 16px; }
  .card--back .brand__name { font-size: 38px; }
  .card--back .brand__tagline { left: 162px; top: 106px; font-size: 8px; letter-spacing: 2.2px; }

  .person { position: absolute; right: 231px; top: 189px; text-align: right; }
  .person__name { font-weight: 700; font-size: 18px; color: var(--accent-orange); letter-spacing: .3px; white-space: nowrap; }
  .person__role { font-weight: 700; font-size: 11px; color: var(--accent-blue); margin-top: 5px; }

  .contacts { position: absolute; left: 305px; top: 188px; list-style: none; }
  .contacts li {
    display: flex; align-items: center;
    height: 15.3px;
    font-size: 11.5px;
    color: var(--accent-orange);
    white-space: nowrap;
  }
  .contacts svg { width: 10px; height: 10px; margin-right: 7px; fill: var(--accent-blue); flex: none; }
</style>
</head>
<body>

<section class="card card--front" aria-label="Card front">
  <div class="brand">
    <span class="brand__dot"></span>
    <span class="brand__name">BrightQuill</span>
  </div>
  <p class="brand__tagline">WRITE YOUR NEXT CHAPTER</p>
  <p class="services">ADVERTISING | SALES | EVENTS | PRODUCTION</p>
</section>

<section class="card card--back" aria-label="Card back">
  <div class="brand">
    <span class="brand__dot"></span>
    <span class="brand__name">BrightQuill</span>
  </div>
  <p class="brand__tagline">WRITE YOUR NEXT CHAPTER</p>

  <div class="person">
    <p class="person__name">MARCUS DUNNE</p>
    <p class="person__role">Managing Director</p>
  </div>

  <ul class="contacts">
    <li><svg viewBox="0 0 10 10" aria-hidden="true"><path d="M1 3.5C1 2 2.5 1 5 1s4 1 4 2.5L7.5 4.5 6.5 3h-3L2.5 4.5z"/><rect x="2" y="5" width="6" height="4" rx="1"/></svg>1300 586 231</li>
    <li><svg viewBox="0 0 10 10" aria-hidden="true"><rect x="3" y="0.5" width="4" height="9" rx="1"/></svg>0407 862 553</li>
    <li><svg viewBox="0 0 10 10" aria-hidden="true"><rect x="2.5" y="0.5" width="5" height="3"/><rect x="0.5" y="3.5" width="9" height="4.5" rx="1"/><rect x="2.5" y="7" width="5" height="2.5"/></svg>(02) 8361 2490</li>
    <li><svg viewBox="0 0 10 10" aria-hidden="true"><path d="M5 0.5a4.5 4.5 0 1 0 2.6 8.2l-.5-.8A3.5 3.5 0 1 1 8.5 5v.7c0 .6-.4 1-.9 1s-.8-.4-.8-1V3h-1v.4A2 2 0 1 0 6.9 6.6 1.8 1.8 0 0 0 9.5 5.7V5A4.5 4.5 0 0 0 5 .5zm0 5.6a1.1 1.1 0 1 1 0-2.2 1.1 1.1 0 0 1 0 2.2z"/></svg>marcus@brightquill.com.au</li>
    <li><svg viewBox="0 0 10 10" aria-hidden="true"><path d="M5 .5a4.5 4.5 0 1 0 0 9 4.5 4.5 0 0 0 0-9zm0 1c.6.6 1 1.7 1.1 3H3.9C4 3.2 4.4 2.1 5 1.5zM2.9 4.5h-1.3a3.5 3.5 0 0 1 2-2.7 6 6 0 0 0-.7 2.7zm0 1a6 6 0 0 0 .7 2.7 3.5 3.5 0 0 1-2-2.7zm1 0h2.2c-.1 1.3-.5 2.4-1.1 3-.6-.6-1-1.7-1.1-3zm3.2 0h1.3a3.5 3.5 0 0 1-2 2.7 6 6 0 0 0 .7-2.7zm0-1a6 6 0 0 0-.7-2.7 3.5 3.5 0 0 1 2 2.7z"/></svg>www.brightquill.com.au</li>
  </ul>
</section>

</body>
</html>
```